M&A Advisory firm needs elegant and powerful letterhead

We need a powerful but elegant letterhead to engage with the international financial industry.

Target Market(s)

New York and International Financial Industry

Industry/Entity Type

Finance

Font styles to use
Other font styles liked:
• Poppins

Requirements
Must have
• 482 W 71st Street 14th Floor New York, NY 10157 O: +1 (212) 555 0147 F: +1 (212) 555 0182

```html
<!DOCTYPE html>
<html lang="en">
<head>
<meta charset="utf-8">
<title>Meridane Letterhead</title>
<link rel="stylesheet" href="https://fonts.googleapis.com/css2?family=Poppins:wght@400&family=Montserrat:wght@600&family=Questrial&family=Open+Sans:wght@600&family=Lato:wght@400&display=swap">
<style>
  :root {
    --brand-blue: #0d4f94;
    --ink-grey: #8e8e8e;
    --name-grey: #9b9b9b;
    --rule-grey: #8a8a8a;
    --backdrop: #ecedef;
    --paper: #ffffff;
  }
  * { margin: 0; padding: 0; box-sizing: border-box; }
  html, body { width: 1068px; height: 1200px; overflow: hidden; background: var(--backdrop); }
  .letterhead {
    position: absolute; left: 106px; top: 0;
    width: 855px; height: 1200px;
    background: var(--paper);
    color: var(--ink-grey);
  }
  .brand {
    position: absolute; left: 37px; top: 76px;
    display: flex; align-items: center; gap: 14px;
  }
  .brand-dot { width: 44px; height: 44px; border-radius: 50%; background: var(--brand-blue); }
  .brand-name {
    font-family: "Poppins", sans-serif; font-weight: 400;
    font-size: 56px; line-height: 1; color: var(--brand-blue); letter-spacing: 0.5px;
  }
  .sender { position: absolute; left: 68px; top: 304px; font-family: "Montserrat", sans-serif; }
  .sender-name { font-weight: 600; font-size: 24px; color: var(--name-grey); letter-spacing: 0.5px; margin-bottom: 6px; }
  .sender-line { font-family: "Lato", sans-serif; font-size: 14px; line-height: 19px; color: var(--ink-grey); margin-bottom: 7px; }
  .sender-line.address { margin-bottom: 0; }
  .letter-date {
    position: absolute; right: 64px; top: 406px;
    font-family: "Open Sans", sans-serif; font-weight: 600; font-size: 15.5px; color: var(--ink-grey);
  }
  .letter-body {
    position: absolute; left: 64px; top: 461px; width: 727px;
    font-family: "Questrial", sans-serif; font-size: 14.6px; line-height: 18.5px;
    text-align: justify; color: var(--ink-grey);
  }
  .letter-body p { margin-bottom: 18.5px; }
  .letter-body p.spaced { margin-top: 18px; }
  .sign-off {
    position: absolute; left: 559px; top: 833px;
    font-family: "Questrial", sans-serif; font-size: 21px; color: var(--ink-grey);
  }
  .signature {
    position: absolute; left: 573px; top: 876px; width: 150px; height: 95px;
    background: linear-gradient(135deg, #f4f4f4, #e4e4e4);
  }
  .contact-bar {
    position: absolute; left: 95px; top: 1113px;
    display: flex; align-items: center;
    font-family: "Lato", sans-serif; font-size: 15px; color: #6d6d6d;
  }
  .contact-item { display: flex; align-items: center; gap: 6px; margin-right: 14px; }
  .contact-icon { width: 18px; height: 18px; }
  .footer-rule { position: absolute; left: 0; bottom: 27px; width: 855px; height: 12px; }
</style>
</head>
<body>
<main class="letterhead">
  <header class="brand">
    <span class="brand-dot"></span>
    <span class="brand-name">Meridane</span>
  </header>

  <section class="sender">
    <h1 class="sender-name">CLARA WHITFIELD</h1>
    <p class="sender-line">0123-555-014</p>
    <p class="sender-line">hello@meridaneadvisory.com</p>
    <p class="sender-line address">5610 Cedar Crest Ln. Suite<br>210 Dallas, TX 75201</p>
  </section>

  <p class="letter-date">12 December, 2023</p>

  <article class="letter-body">
    <p>Lorem ipsum dolor sit amet, consectetuer adipiscing elit, sed diam nonummy nibh euismod tincidunt ut laoreet dolore magna aliquam erat volutpat. Ut wisi enim ad minim veniam, quis nostrud exerci tation ullamcorper suscipit lobortis nisl ut aliquip ex ea commodo consequat. Duis autem vel eum iriure dolor in hendrerit in vulputate velit esse molestie consequat, vel illum dolore eu feugiat nulla facilisis at vero eros et accumsan et iusto odio dignissim qui blandit praesent luptatum zzril delenit augue duis dolore te feugait nulla facilisi.</p>
    <p>Lorem ipsum dolor sit amet, cons ectetuer adipiscing elit, sed diam nonummy nibh euismod tincidunt ut laoreet dolore magna aliquam erat volutpat. Ut wisi enim ad minim veniam, quis nostrud exerci tation ullamcorper suscipit lobortis nisl ut aliquip ex ea commodo consequat.<br>Lorem ipsum dolor sit amet, consectetuer adipiscing elit, sed diam nonummy nibh euismod tincidunt ut laoreet dolore magna aliquam erat</p>
    <p class="spaced">Lorem ipsum dolor sit amet, cons ectetuer adipiscing elit, sed diam nonummy nibh euismod tincidunt ut laoreet dolore magna aliquam erat volutpat. Ut wisi enim ad minim veniam, quis nostrud exerci tation ullamcorper suscipit lobortis nisl ut aliquip ex ea commodo consequat. Lorem ipsum dolor sit zamet, consectetuer adipiscing elit, sed diam nonummy nibh euismod tincidunt.</p>
  </article>

  <p class="sign-off">Managing Director</p>
  <div class="signature" role="img" aria-label="Handwritten signature of the managing director"></div>

  <footer class="contact-bar">
    <span class="contact-item">
      <svg class="contact-icon" viewBox="0 0 18 18" aria-hidden="true">
        <rect width="18" height="18" rx="2.5" fill="var(--brand-blue)"/>
        <path d="M5.2 3.6l2 .3.7 2.6-1.3 1a7 7 0 0 0 3.9 3.9l1-1.3 2.6.7.3 2c-.1.9-.9 1.5-1.8 1.4A10 10 0 0 1 3.8 5.4c-.1-.9.5-1.7 1.4-1.8z" fill="#fff"/>
      </svg>
      +1 (212) 555 0147
    </span>
    <span class="contact-item">
      <svg class="contact-icon" viewBox="0 0 18 18" aria-hidden="true">
        <rect width="18" height="18" rx="2.5" fill="var(--brand-blue)"/>
        <rect x="5.5" y="3.5" width="7" height="4" fill="none" stroke="#fff" stroke-width="1.2"/>
        <rect x="3" y="7.5" width="12" height="5" rx="1" fill="none" stroke="#fff" stroke-width="1.2"/>
        <rect x="5.5" y="11" width="7" height="4" fill="var(--brand-blue)" stroke="#fff" stroke-width="1.2"/>
      </svg>
      +1 (212) 555 0182
    </span>
    <span class="contact-item">
      <svg class="contact-icon" viewBox="0 0 18 18" aria-hidden="true">
        <rect width="18" height="18" rx="2.5" fill="var(--brand-blue)"/>
        <path d="M9 3a4 4 0 0 1 4 4c0 3-4 8-4 8S5 10 5 7a4 4 0 0 1 4-4z" fill="#fff"/>
        <circle cx="9" cy="7" r="1.5" fill="var(--brand-blue)"/>
      </svg>
      482 W 71st Street 14th Floor New York, NY 10157
    </span>
  </footer>

  <svg class="footer-rule" viewBox="0 0 855 12" preserveAspectRatio="none" aria-hidden="true">
    <rect x="0" y="6" width="486" height="5" fill="var(--rule-grey)"/>
    <polygon points="492,1 855,1 855,11 484,11" fill="var(--brand-blue)"/>
  </svg>
</main>
</body>
</html>
```